German Webagency needs fresh modern Design

Our website is 4 years old. We need an fresh modern website. All pics we used before are from customers or handmade by us. the new website should be clear with nice handling. please dont copy something from template websites. it would be great if you can surprise us with something great. its our first project here. don´t worry if i make a mistake in responding or briefing. after 20 years you can´t see the works of your own "designer" so we hope for help :-)
our existing site: www.tovankreativ.de
Target Market(s)
small and middle sized companys in germany
Number of Pages Required
4 page
Font styles to use
Colors
Designer to choose colors to be used in the design.
Requirements
Must have
- Responsive (sure we code it)
- Modern and big Font ..Headlines and Slider
- innovative..if you know something new..feel free to show
Nice to have
- the site with our works/refences should look great and later easy to handle when we code it or use wp.
- we like black and grey but if you have better ideas also feel free
Should not have
- a cup of coffe..laptop.. a pencil a handwritten font
- dont copy and modify templates from know websites..bad style

```html
<!DOCTYPE html>
<html lang="en">
<head>
<meta charset="utf-8">
<title>Tovan Kreativ – Web Agency</title>
<link href="https://fonts.googleapis.com/css2?family=Open+Sans:ital,wght@0,300;0,400;0,600;0,700;0,800;1,700;1,800&display=swap" rel="stylesheet">
<style>
:root{
  --blue:#2f7cc4;
  --blue-dark:#1f5f9e;
  --sky:#36a6d8;
  --green:#6cbf4a;
  --ink:#2a2a2a;
  --text:#666666;
  --soft:#f2f2f2;
  --line:#dddddd;
  --white:#ffffff;
  --bar:#2b2b2b;
}
*{box-sizing:border-box;margin:0;padding:0}
html,body{width:1200px;height:3822px;overflow:hidden}
body{font-family:"Open Sans",Arial,sans-serif;color:var(--text);background:var(--white);position:relative}
.abs{position:absolute}
section,header,footer{position:absolute;left:0;width:1200px}
p.lorem{font-size:14px;line-height:26px;color:var(--text)}
.btn{display:inline-block;background:var(--blue);color:var(--white);font-size:13px;font-weight:600;letter-spacing:1px;text-transform:uppercase;padding:0 24px;line-height:36px;border-radius:3px}
.section-title{font-size:36px;font-weight:300;color:var(--ink);text-transform:uppercase;text-align:center;letter-spacing:2px;line-height:44px}
.section-title strong{font-weight:700}
.title-rule{width:60px;height:3px;background:var(--blue);margin:14px auto 0}

/* header */
.site-header{top:0;height:132px;border-top:5px solid var(--blue);background:var(--white)}
.brand{left:92px;top:44px;display:flex;align-items:center;gap:10px}
.brand-dot{width:22px;height:22px;border-radius:50%;background:var(--blue)}
.brand-name{font-size:32px;font-weight:800;color:var(--ink);letter-spacing:-.5px}
.main-nav{right:88px;top:58px;display:flex;font-size:13px;font-weight:600;letter-spacing:.5px;text-transform:uppercase}
.main-nav a{color:var(--ink);text-decoration:none;padding:0 30px;border-left:1px solid #999;line-height:14px}
.main-nav a:first-child{border-left:none;padding-left:0}
.main-nav a.active{position:relative;color:var(--blue)}
.main-nav a.active::after{content:"";position:absolute;left:0;right:30px;bottom:-14px;height:3px;background:var(--blue)}

/* hero */
.hero{top:132px;height:513px}
.hero-text{left:655px;top:132px;width:500px}
.hero-text h1{font-style:italic;font-weight:800;font-size:33px;line-height:42px;color:var(--blue);margin-bottom:14px;letter-spacing:-.5px;white-space:nowrap}
.hero-text p{font-size:15px;line-height:25px;color:#333;margin-bottom:20px}
.slider-arrow{width:40px;height:40px;border-radius:50%;background:rgba(255,255,255,.55);top:236px;display:flex;align-items:center;justify-content:center}

/* welcome */
.welcome{top:645px;height:323px;background:var(--soft);text-align:center}
.welcome h2{font-size:34px;font-weight:300;color:var(--ink);line-height:40px;margin-top:34px;letter-spacing:1px}
.welcome h2 .accent{color:var(--blue);font-weight:800}
.welcome p.lorem{width:1030px;margin:16px auto 24px}

/* services */
.services{top:968px;height:489px}
.services .section-title{margin-top:40px}
.service-grid{left:99px;top:122px;width:1002px;height:244px;display:flex;border:1px solid var(--line)}
.service-card{flex:1;border-left:1px solid var(--line);text-align:center;padding-top:25px}
.service-card:first-child{border-left:none}
.service-icon{width:126px;height:126px;border-radius:50%;border:3px solid var(--green);margin:0 auto 18px;display:flex;align-items:center;justify-content:center}
.service-card h3{font-size:17px;font-weight:600;color:var(--ink);text-transform:uppercase;line-height:25px;letter-spacing:.5px}
.carousel-nav{left:552px;top:405px;display:flex;gap:14px}
.carousel-nav span{width:40px;height:40px;border:2px solid #555;border-radius:50%;display:flex;align-items:center;justify-content:center}

/* stats */
.stats{top:1457px;height:360px;background:linear-gradient(120deg,#2ea0d6 0%,#3cb0df 50%,#2a95cc 100%)}
.stat{width:160px;text-align:center;top:112px;color:var(--white)}
.stat svg{display:block;margin:0 auto 12px}
.stat strong{font-size:42px;font-weight:800;letter-spacing:-.5px}

/* feature rows */
.feature{height:344px}
.feature h2{font-size:30px;font-weight:300;color:var(--ink);text-transform:uppercase;margin-bottom:16px;letter-spacing:1px;line-height:38px}
.feature h2 strong{font-weight:700}
.web-dev{top:1817px;background:var(--white)}
.social{top:2161px;height:362px;background:var(--soft)}

/* articles */
.articles{top:2523px;height:611px}
.articles .section-title{margin-top:36px}
.article{top:127px;width:324px}
.article-photo{height:229px}
.article h3{font-size:18px;font-weight:700;color:var(--ink);margin:20px 0 8px}
.article p.lorem{font-size:13.5px;line-height:24px}
.article-meta{margin-top:18px;border-top:2px solid var(--line);border-bottom:2px solid var(--line);height:50px;display:flex;justify-content:space-between;align-items:center;font-size:12.5px}
.article-meta a{color:var(--blue);text-decoration:none;font-weight:600}

/* contact */
.contact{top:3134px;height:484px;background:linear-gradient(120deg,#3b86cf 0%,#2f7cc4 50%,#276cb0 100%);color:var(--white);text-align:center}
.contact h2{font-size:42px;font-weight:300;margin-top:40px;text-transform:uppercase;letter-spacing:2px;line-height:54px}
.contact h2 strong{font-weight:800}
.contact p{font-size:14px;line-height:24px;width:640px;margin:10px auto 0}
.field{background:var(--white);color:#888;font-size:13px;text-align:left;padding:0 12px;display:flex;align-items:center;border-radius:2px}
.submit{background:#000;color:var(--white);font-size:13px;font-weight:600;letter-spacing:1px;text-transform:uppercase;display:flex;align-items:center;justify-content:center}

/* footer */
.site-footer{top:3618px;height:148px;background:var(--white)}
.contact-line{left:87px;display:flex;align-items:center;gap:16px;font-size:14px;color:var(--ink)}
.social-links{right:88px;top:57px;display:flex;gap:10px}
.social-links span{width:34px;height:34px;border-radius:50%;background:#8a8a8a}
.bottom-bar{top:3766px;height:56px;background:var(--bar);color:var(--white);font-size:13px;text-align:center;line-height:56px}
.bottom-bar .accent{color:var(--sky)}
</style>
</head>
<body>

<header class="site-header">
  <div class="brand abs"><span class="brand-dot"></span><span class="brand-name">tovankreativ.de</span></div>
  <nav class="main-nav abs">
    <a class="active">Home</a><a>About Us</a><a>Services</a><a>Blog</a><a>Contact Us</a>
  </nav>
</header>

<section class="hero">
  <div class="abs" role="img" aria-label="Businessman working on a laptop in a bright office with city towers behind" style="left:0;top:0;width:1200px;height:513px;background:linear-gradient(90deg,#6d737b 0%,#9aa2aa 30%,#d6dde3 60%,#bfcfdb 100%)"></div>
  <div class="slider-arrow abs" style="left:10px"><svg width="14" height="14" viewBox="0 0 14 14"><path d="M9 2L4 7l5 5" stroke="#fff" stroke-width="2.5" fill="none"/></svg></div>
  <div class="slider-arrow abs" style="right:10px"><svg width="14" height="14" viewBox="0 0 14 14"><path d="M5 2l5 5-5 5" stroke="#fff" stroke-width="2.5" fill="none"/></svg></div>
  <div class="hero-text abs">
    <h1>Strategy-Creativity-Results</h1>
    <p>Lorem Ipsum is simply dummy text of the printing and typesetting industry. Lorem Ipsum has been the industry's standard dummy text ever since the 1500s.</p>
    <span class="btn">Contact Us</span>
  </div>
</section>

<section class="welcome">
  <h2>WELCOME TO<br><span class="accent">TOVAN KREATIV</span></h2>
  <p class="lorem">Lorem Ipsum is simply dummy text of the printing and typesetting industry. Lorem Ipsum has been the industry's standard dummy text ever since the 1500s, when an unknown printer took a galley of type and scrambled it to make a type specimen book. It has survived not only five centuries, but also the leap into electronic typesetting, remaining essentially unchanged.</p>
  <span class="btn">Read More</span>
</section>

<section class="services">
  <h2 class="section-title">Our <strong>Services</strong></h2>
  <div class="title-rule"></div>
  <div class="service-grid abs">
    <div class="service-card">
      <div class="service-icon"><svg width="70" height="60" viewBox="0 0 70 60"><rect x="3" y="3" width="64" height="42" rx="3" fill="none" stroke="#1f5f9e" stroke-width="5"/><path d="M14 35l12-12 9 8 18-16" stroke="#1f5f9e" stroke-width="4" fill="none"/><rect x="28" y="47" width="14" height="6" fill="#1f5f9e"/><rect x="20" y="53" width="30" height="4" fill="#1f5f9e"/></svg></div>
      <h3>Search Engine<br>Optimization</h3>
    </div>
    <div class="service-card">
      <div class="service-icon"><svg width="64" height="64" viewBox="0 0 64 64"><path d="M10 30l30-18v36L10 36z" fill="#1f5f9e"/><rect x="4" y="28" width="8" height="10" fill="#1f5f9e"/><path d="M16 38l6 16h6l-4-14z" fill="#1f5f9e"/><path d="M46 24l10-6M48 30h12M46 36l10 6" stroke="#1f5f9e" stroke-width="4"/></svg></div>
      <h3>Social Media<br>Marketing</h3>
    </div>
    <div class="service-card">
      <div class="service-icon"><svg width="70" height="60" viewBox="0 0 70 60"><rect x="3" y="3" width="64" height="42" rx="3" fill="none" stroke="#1f5f9e" stroke-width="5"/><path d="M24 16l-8 8 8 8M46 16l8 8-8 8M38 14l-6 20" stroke="#1f5f9e" stroke-width="4" fill="none"/><rect x="28" y="47" width="14" height="6" fill="#1f5f9e"/><rect x="20" y="53" width="30" height="4" fill="#1f5f9e"/></svg></div>
      <h3>Web<br>Development</h3>
    </div>
    <div class="service-card">
      <div class="service-icon"><svg width="70" height="50" viewBox="0 0 70 50"><rect x="3" y="3" width="64" height="44" rx="3" fill="none" stroke="#1f5f9e" stroke-width="5"/><rect x="12" y="13" width="16" height="18" fill="#1f5f9e"/><path d="M34 15h24M34 24h24M34 33h16M12 38h16" stroke="#1f5f9e" stroke-width="4"/></svg></div>
      <h3>Business<br>Cards</h3>
    </div>
    <div class="service-card">
      <div class="service-icon"><svg width="60" height="60" viewBox="0 0 60 60"><rect x="6" y="36" width="10" height="18" fill="#1f5f9e"/><rect x="22" y="26" width="10" height="28" fill="#1f5f9e"/><rect x="38" y="14" width="10" height="40" fill="#1f5f9e"/><path d="M4 56h52" stroke="#1f5f9e" stroke-width="4"/></svg></div>
      <h3>Paid Search<br>Ads</h3>
    </div>
  </div>
  <div class="carousel-nav abs">
    <span><svg width="12" height="12" viewBox="0 0 12 12"><path d="M8 1L3 6l5 5" stroke="#555" stroke-width="2" fill="none"/></svg></span>
    <span><svg width="12" height="12" viewBox="0 0 12 12"><path d="M4 1l5 5-5 5" stroke="#555" stroke-width="2" fill="none"/></svg></span>
  </div>
</section>

<section class="stats" role="img" aria-label="Blue tinted office desk with laptop, backing four performance figures">
  <div class="stat abs" style="left:124px">
    <svg width="72" height="62" viewBox="0 0 72 62"><rect x="3" y="3" width="66" height="44" rx="3" fill="none" stroke="#fff" stroke-width="5"/><path d="M26 16l-8 9 8 9M46 16l8 9-8 9M39 14l-6 22" stroke="#fff" stroke-width="4" fill="none"/><rect x="29" y="48" width="14" height="7" fill="#fff"/><rect x="20" y="55" width="32" height="4" fill="#fff"/></svg>
    <strong>100%</strong>
  </div>
  <div class="stat abs" style="left:384px">
    <svg width="72" height="62" viewBox="0 0 72 62"><rect x="3" y="12" width="56" height="44" fill="none" stroke="#fff" stroke-width="5"/><path d="M22 44l6-12 34-30 6 6-34 30z" fill="#fff"/></svg>
    <strong>95%</strong>
  </div>
  <div class="stat abs" style="left:654px">
    <svg width="72" height="62" viewBox="0 0 72 62"><path d="M4 58V40l14-8v26zM22 58V30l14-10v38zM40 58V24l12-8 4 6v36z" fill="#fff"/><path d="M4 30L30 12l14 8 24-16" stroke="#fff" stroke-width="4" fill="none"/></svg>
    <strong>100%</strong>
  </div>
  <div class="stat abs" style="left:911px">
    <svg width="72" height="62" viewBox="0 0 72 62"><circle cx="36" cy="22" r="7" fill="#fff"/><path d="M24 46c0-10 24-10 24 0z" fill="#fff"/><circle cx="14" cy="10" r="7" fill="#fff"/><circle cx="58" cy="10" r="7" fill="#fff"/><circle cx="12" cy="50" r="7" fill="#fff"/><circle cx="60" cy="50" r="7" fill="#fff"/><path d="M18 14l12 5M54 14l-12 5M16 46l8-4M56 46l-8-4" stroke="#fff" stroke-width="2"/></svg>
    <strong>98%</strong>
  </div>
</section>

<section class="feature web-dev">
  <div class="abs" style="left:82px;top:100px;width:540px">
    <h2><strong>Web Development</strong> &amp; SEO</h2>
    <p class="lorem">Lorem Ipsum is simply dummy text of the printing and typesetting industry. Lorem Ipsum has been the industry's standard dummy text ever since the 1500s, when an unknown printer took a galley of type and scrambled.</p>
  </div>
  <div class="abs" role="img" aria-label="Illustration of laptop, desktop monitor, tablet and phone showing charts" style="left:668px;top:69px;width:453px;height:204px;background:linear-gradient(180deg,#e4e7ea 0%,#c9ced3 100%);border-radius:6px"></div>
</section>

<section class="feature social">
  <div class="abs" role="img" aria-label="Top view of a team gathered around a round table with social media sign" style="left:132px;top:35px;width:296px;height:301px;border-radius:50%;background:radial-gradient(circle,#d3a25a 0%,#b8844a 55%,#4b4f63 100%)"></div>
  <div class="abs" style="left:571px;top:110px;width:540px">
    <h2><strong>Social Media</strong> Marketing</h2>
    <p class="lorem">Lorem Ipsum is simply dummy text of the printing and typesetting industry. Lorem Ipsum has been the industry's standard dummy text ever since the 1500s, when an unknown printer took a galley of type and scrambled.</p>
  </div>
</section>

<section class="articles">
  <h2 class="section-title">Recent <strong>Articles</strong></h2>
  <article class="article abs" style="left:87px">
    <div class="article-photo" role="img" aria-label="Laptop on a desk showing code" style="background:linear-gradient(135deg,#3a3f45 0%,#7a8087 60%,#c7ccd0 100%)"></div>
    <h3>HEADING TITLE HERE</h3>
    <p class="lorem">Lorem Ipsum is simply dummy text of the printing and typesetting industry. Lorem Ipsum has been the industry's standard dummy text ever since the 1500s.</p>
    <div class="article-meta"><a>READ MORE ▸</a><span>16/DEC/2018</span></div>
  </article>
  <article class="article abs" style="left:438px">
    <div class="article-photo" role="img" aria-label="Team working together around a wooden table from above" style="background:linear-gradient(135deg,#6b4a32 0%,#a57a52 55%,#d8c3a5 100%)"></div>
    <h3>HEADING TITLE HERE</h3>
    <p class="lorem">Lorem Ipsum is simply dummy text of the printing and typesetting industry. Lorem Ipsum has been the industry's standard dummy text ever since the 1500s.</p>
    <div class="article-meta"><a>READ MORE ▸</a><span>16/DEC/2018</span></div>
  </article>
  <article class="article abs" style="left:787px">
    <div class="article-photo" role="img" aria-label="Business meeting in a conference room with a presentation screen" style="background:linear-gradient(135deg,#d9dde0 0%,#8f8478 55%,#3e3833 100%)"></div>
    <h3>HEADING TITLE HERE</h3>
    <p class="lorem">Lorem Ipsum is simply dummy text of the printing and typesetting industry. Lorem Ipsum has been the industry's standard dummy text ever since the 1500s.</p>
    <div class="article-meta"><a>READ MORE ▸</a><span>16/DEC/2018</span></div>
  </article>
</section>

<section class="contact">
  <h2>Contact <strong>Us</strong></h2>
  <p>Lorem Ipsum is simply dummy text of the printing and typesetting industry. Lorem Ipsum has been the industry's standard dummy text ever since the 1500s.</p>
  <div class="field abs" style="left:87px;top:206px;width:499px;height:174px;align-items:flex-start;padding-top:12px">Message</div>
  <div class="field abs" style="left:617px;top:206px;width:499px;height:44px">Name</div>
  <div class="field abs" style="left:617px;top:273px;width:499px;height:44px">Email</div>
  <div class="field abs" style="left:617px;top:339px;width:334px;height:44px;justify-content:space-between">Type the code shown<strong style="color:#222">HG845</strong></div>
  <div class="submit abs" style="left:971px;top:339px;width:145px;height:44px">Submit</div>
</section>

<footer class="site-footer">
  <div class="contact-line abs" style="top:44px">
    <svg width="16" height="16" viewBox="0 0 16 16"><path d="M3 1h3l1 4-2 1c1 2 3 4 5 5l1-2 4 1v3c0 1-1 2-2 2C7 15 1 9 1 3c0-1 1-2 2-2z" fill="#1f5f9e"/></svg>123-456-789
  </div>
  <div class="contact-line abs" style="top:83px">
    <svg width="16" height="12" viewBox="0 0 16 12"><rect width="16" height="12" rx="1" fill="#1f5f9e"/><path d="M1 1l7 6 7-6" stroke="#fff" stroke-width="1.5" fill="none"/></svg>info@domain.com
  </div>
  <div class="social-links abs"><span></span><span></span><span></span></div>
</footer>

<div class="bottom-bar abs" style="left:0;width:1200px">© 2018 <span class="accent">tovankreativ.de</span> | All rights reserved.</div>

</body>
</html>
```